Business card design to suit our website

Need a nice looking business card for our business based off images from our Website and provided images. The business card will require 2 different names (for the 2 owners). The business card should include images from our website, facebook (keel bracket works set) or the pictures provided. it should also contain all contact information.
Our website is www.keelbracketworks.com.au
Please dont use image from top bar of website. If images are used please use the ones of our product under the buy it now tab

Target Market(s)

Automotive

Industry/Entity Type

Automotive Part

Contact Information for Business Card

Business Name. contact details including names phone number email. logo
2 business cards needed with 2 different persons names and phone number.

Colors

Designer to choose colors to be used in the design.

Requirements
Must have
• whatever looks best

```html
<!DOCTYPE html>
<html lang="en">
<head>
<meta charset="utf-8">
<title>Steadfast Keel Bracket Works Set – Business Cards</title>
<link rel="stylesheet" href="https://fonts.googleapis.com/css2?family=Open+Sans:ital,wght@0,400;0,600;0,800;1,700&display=swap">
<style>
  :root {
    --stage: #232323;
    --card-top: #1d1d1f;
    --card-bottom: #0b0b0c;
    --brand-red: #c8202f;
    --tread-red: #a81a26;
    --ink-white: #f4f4f4;
    --ink-grey: #d8d8d8;
  }
  * { box-sizing: border-box; margin: 0; padding: 0; }
  html, body {
    width: 1200px; height: 900px; overflow: hidden;
    background: var(--stage);
    font-family: "Open Sans", Arial, sans-serif;
  }
  .stage { position: relative; width: 1200px; height: 900px; }

  .card {
    position: absolute;
    width: 700px; height: 400px;
    border-radius: 26px;
    overflow: hidden;
    background: radial-gradient(ellipse at 40% 30%, var(--card-top), var(--card-bottom) 75%);
    box-shadow: 0 18px 40px rgba(0,0,0,.55);
  }
  .card--front { left: 440px; top: 50px; }
  .card--back  { left: 60px;  top: 450px; }

  .tread {
    position: absolute;
    background: var(--tread-red);
  }
  .band {
    position: absolute;
    right: 0;
    background: var(--brand-red);
    display: flex; align-items: center;
  }
  .band__text {
    color: var(--ink-white);
    font-weight: 700; font-style: italic;
    white-space: nowrap;
  }
  .brand {
    position: absolute;
    display: flex; align-items: center; gap: 12px;
  }
  .brand__dot {
    flex: none;
    border-radius: 50%;
    background: var(--brand-red);
  }
  .brand__name {
    color: var(--brand-red);
    font-weight: 800;
    line-height: 1;
    white-space: nowrap;
  }

  /* front */
  .card--front .tread--upper { left: 60px; top: 120px; width: 200px; height: 18px; }
  .card--front .tread--lower { left: 60px; top: 146px; width: 200px; height: 34px; }
  .card--front .brand { left: 270px; top: 100px; }
  .card--front .brand__dot { width: 24px; height: 24px; }
  .card--front .brand__name { font-size: 60px; }
  .card--front .band { left: 300px; top: 190px; height: 50px; padding-left: 30px; }
  .card--front .band__text { font-size: 28px; }
  .website {
    position: absolute; left: 330px; top: 262px;
    color: var(--brand-red); font-size: 16px; letter-spacing: .3px;
  }

  /* back */
  .card--back .tread--upper { left: 110px; top: 78px; width: 190px; height: 16px; }
  .card--back .tread--lower { left: 110px; top: 100px; width: 190px; height: 28px; }
  .card--back .brand { left: 310px; top: 60px; }
  .card--back .brand__dot { width: 20px; height: 20px; }
  .card--back .brand__name { font-size: 50px; }
  .card--back .band { left: 300px; top: 134px; height: 40px; padding-left: 24px; }
  .card--back .band__text { font-size: 22px; }

  .contact {
    position: absolute; right: 40px; top: 200px;
    text-align: right;
  }
  .contact__name { color: var(--ink-white); font-size: 36px; font-weight: 600; line-height: 1.1; }
  .contact__role { color: var(--brand-red); font-size: 20px; margin-bottom: 16px; }
  .contact__line {
    display: flex; justify-content: flex-end; align-items: center; gap: 10px;
    color: var(--ink-grey); font-size: 20px; line-height: 1.6;
  }
  .contact__icon { width: 20px; height: 20px; fill: var(--brand-red); }
</style>
</head>
<body>
<main class="stage">

  <section class="card card--front" aria-label="Business card front">
    <div class="tread tread--upper" role="img" aria-label="Tyre tread track"></div>
    <div class="tread tread--lower" role="img" aria-label="Tyre tread track"></div>
    <div class="brand">
      <span class="brand__dot"></span>
      <span class="brand__name">Steadfast</span>
    </div>
    <div class="band"><span class="band__text">Keel Bracket Works Set</span></div>
    <p class="website">www.keelbracketworks.com.au</p>
  </section>

  <section class="card card--back" aria-label="Business card back">
    <div class="tread tread--upper" role="img" aria-label="Tyre tread track"></div>
    <div class="tread tread--lower" role="img" aria-label="Tyre tread track"></div>
    <div class="brand">
      <span class="brand__dot"></span>
      <span class="brand__name">Steadfast</span>
    </div>
    <div class="band"><span class="band__text">Keel Bracket Works Set</span></div>

    <div class="contact">
      <p class="contact__name">Your Name</p>
      <p class="contact__role">Job Title</p>
      <p class="contact__line">000 0000 0000
        <svg class="contact__icon" viewBox="0 0 20 20" aria-hidden="true">
          <path d="M2 6c0-2 3-3 8-3s8 1 8 3v2h-4V6.5c-1-.5-2.5-.7-4-.7s-3 .2-4 .7V8H2z"/>
          <path d="M4 10h12l1 7H3z"/>
        </svg>
      </p>
      <p class="contact__line">youremail@xyz.com
        <svg class="contact__icon" viewBox="0 0 20 20" aria-hidden="true">
          <path d="M2 4h16v12H2z M3.5 5.5 10 11l6.5-5.5" stroke="#0b0b0c" stroke-width="1.4"/>
        </svg>
      </p>
    </div>
  </section>

</main>
</body>
</html>
```